Bref créative
Business Card and Stationary Design
Brevard Advisory Ltd.
Professional
Duncan Morvell
19 Pine Terrace
Redmarsh, AB T3K 6B9
duncan@brevardadvisory.example
www.brevardadvisory.example
I would like a design that includes some color.
I very much prefer the text to be very readable (clear, large).
I would like the back of the card to include the logo and some color.
Brevard Advisory Ltd. logo. AI format.

```html
<!DOCTYPE html>
<html lang="en">
<head>
<meta charset="utf-8">
<title>Brevard Advisory Ltd. — Stationery</title>
<link href="https://fonts.googleapis.com/css2?family=Roboto+Condensed:wght@700&family=Open+Sans:wght@400;600&display=swap" rel="stylesheet">
<style>
  :root{
    --navy:#1d3f7a;
    --navy-deep:#122a57;
    --navy-light:#2f5aa3;
    --silver:#c9ced6;
    --paper:#ffffff;
    --ink:#4a4f57;
    --backdrop:#ece8e2;
  }
  *{box-sizing:border-box;margin:0;padding:0}
  html,body{width:1200px;height:862px;overflow:hidden;background:var(--backdrop)}
  .canvas{position:relative;width:1200px;height:862px}
  .sheet{position:absolute;background:var(--paper);box-shadow:0 3px 10px rgba(0,0,0,.18);overflow:hidden}
  .brand{display:flex;align-items:center;gap:8px}
  .brand-dot{width:30px;height:30px;border-radius:50%;background:var(--navy);flex:none}
  .brand-name{font-family:"Roboto Condensed",sans-serif;font-weight:700;color:var(--navy);line-height:1;text-transform:uppercase;white-space:nowrap}
  .brand-name span{display:block}
  .brand-name .l1{font-size:22px;letter-spacing:.5px}
  .brand-name .l2{font-size:12px;letter-spacing:.6px;margin-top:2px}
  .brand.on-dark .brand-dot{background:#fff}
  .brand.on-dark .brand-name{color:#fff}
  .contact{font-family:"Open Sans",sans-serif;font-size:7px;line-height:1.45;color:var(--ink);border-left:1px solid var(--silver);padding-left:10px;white-space:nowrap}
  .header{position:absolute;display:flex;align-items:center;gap:12px}
  .wave{position:absolute;left:0;bottom:0;width:100%}

  .letterhead{left:62px;top:34px;width:464px;height:655px}
  .letterhead .header{left:34px;top:42px}

  .env-back{width:593px;height:343px;left:559px}
  .env-back.top{top:48px}
  .env-back.lower{top:425px;height:295px}
  .env-flap{position:absolute;left:0;top:0;width:100%}
  .flap-name{position:absolute;left:50%;transform:translateX(-50%);font-family:"Roboto Condensed",sans-serif;font-weight:700;font-size:13px;color:#fff;letter-spacing:.6px;text-transform:uppercase}
  .env-front{left:619px;width:533px;height:231px}
  .env-front.top{top:158px}
  .env-front.lower{top:526px;height:220px}
  .env-front .header{left:30px;top:42px}

  .card{width:240px;height:98px}
  .card-front{left:62px;top:725px}
  .card-front .header{left:56px;top:12px;gap:8px}
  .card-front .brand-dot{width:16px;height:16px}
  .card-front .l1{font-size:12px}.card-front .l2{font-size:7px}
  .card-front .contact{font-size:5px;padding-left:6px}
  .card-name{position:absolute;left:14px;top:52px;font-family:"Open Sans",sans-serif;font-weight:600;font-size:9px;color:var(--navy)}
  .card-back{left:329px;top:730px;width:163px;height:93px;background:linear-gradient(180deg,var(--navy-light),var(--navy-deep))}
  .card-back .brand{position:absolute;left:50%;top:50%;transform:translate(-50%,-50%);gap:6px}
  .card-back .brand-dot{width:16px;height:16px}
  .card-back .l1{font-size:12px}.card-back .l2{font-size:7px}
</style>
</head>
<body>
<main class="canvas">

  <section class="sheet letterhead">
    <div class="header">
      <div class="brand"><div class="brand-dot"></div><div class="brand-name"><span class="l1">Brevard</span><span class="l2">Advisory Ltd.</span></div></div>
      <div class="contact">19 Pine Terrace<br>Redmarsh, AB T3K 6B9<br>www.brevardadvisory.example</div>
    </div>
    <svg class="wave" viewBox="0 0 464 70" height="70" preserveAspectRatio="none">
      <path d="M0 30 Q230 0 464 22 L464 30 Q230 10 0 40Z" fill="var(--silver)"/>
      <path d="M0 42 Q230 12 464 32 L464 70 L0 70Z" fill="var(--navy)"/>
    </svg>
  </section>

  <section class="sheet env-back top">
    <svg class="env-flap" viewBox="0 0 593 130" height="130" preserveAspectRatio="none">
      <defs><linearGradient id="flapA" x1="0" y1="0" x2="0" y2="1"><stop offset="0" stop-color="var(--navy-light)"/><stop offset="1" stop-color="var(--navy-deep)"/></linearGradient></defs>
      <path d="M0 0 H593 V20 Q420 60 310 118 Q296 126 283 118 Q173 60 0 20Z" fill="url(#flapA)"/>
    </svg>
    <div class="flap-name" style="top:42px">Brevard</div>
  </section>
  <section class="sheet env-front top">
    <div class="header">
      <div class="brand"><div class="brand-dot"></div><div class="brand-name"><span class="l1">Brevard</span><span class="l2">Advisory Ltd.</span></div></div>
      <div class="contact">19 Pine Terrace<br>Redmarsh, AB T3K 6B9<br>www.brevardadvisory.example</div>
    </div>
  </section>

  <section class="sheet env-back lower">
    <svg class="env-flap" viewBox="0 0 593 120" height="120" preserveAspectRatio="none">
      <defs><linearGradient id="flapB" x1="0" y1="0" x2="0" y2="1"><stop offset="0" stop-color="var(--navy-light)"/><stop offset="1" stop-color="var(--navy-deep)"/></linearGradient></defs>
      <path d="M0 0 H593 V18 Q420 55 310 108 Q296 116 283 108 Q173 55 0 18Z" fill="url(#flapB)"/>
    </svg>
    <div class="flap-name" style="top:40px">Brevard</div>
  </section>
  <section class="sheet env-front lower">
    <div class="header">
      <div class="brand"><div class="brand-dot"></div><div class="brand-name"><span class="l1">Brevard</span><span class="l2">Advisory Ltd.</span></div></div>
      <div class="contact">19 Pine Terrace<br>Redmarsh, AB T3K 6B9<br>www.brevardadvisory.example</div>
    </div>
    <svg class="wave" viewBox="0 0 533 40" height="40" preserveAspectRatio="none">
      <path d="M0 18 Q260 -2 533 14 L533 20 Q260 6 0 26Z" fill="var(--silver)"/>
      <path d="M0 28 Q260 8 533 22 L533 40 L0 40Z" fill="var(--navy)"/>
    </svg>
  </section>

  <section class="sheet card card-front">
    <div class="header">
      <div class="brand"><div class="brand-dot"></div><div class="brand-name"><span class="l1">Brevard</span><span class="l2">Advisory Ltd.</span></div></div>
      <div class="contact">T 403 555 0148<br>duncan@brevardadvisory.example<br>19 Pine Terrace<br>Redmarsh, AB T3K 6B9</div>
    </div>
    <div class="card-name">Duncan Morvell</div>
    <svg class="wave" viewBox="0 0 240 26" height="26" preserveAspectRatio="none">
      <path d="M0 10 Q120 0 240 8 L240 12 Q120 4 0 15Z" fill="var(--silver)"/>
      <path d="M0 16 Q120 5 240 13 L240 26 L0 26Z" fill="var(--navy)"/>
    </svg>
  </section>

  <section class="sheet card card-back">
    <div class="brand on-dark"><div class="brand-dot"></div><div class="brand-name"><span class="l1">Brevard</span><span class="l2">Advisory Ltd.</span></div></div>
  </section>

</main>
</body>
</html>
```